Website Design für Reinigungsunternehmen
Zielgruppe
Wir sind ein Reinigungsunternehmen, dass seit 2014 am Markt ist.
Was machen wir:
Das Angebot besteht darin, Räume nach dem IFSG (Infektionsschutzgesetz) und den Richtlinien des Werner Lasko Instituts mit ausgewählten Verfahren keimfrei zu bekommen.
Hygiene und prophylaktische Desinfektion sind für die Nutzung stark frequentierter Räume und Oberflächen gerade jetzt essentiell, denn die Ausbreitung von Viren und Bakterien kann auch durch präventive Maßnahmen eingedämmt werden.
Das Angebot ist, mit speziellen Reinigungsverfahren in Kombination mit Kaltverneblung ,die Räume fast vollständig von Keimen, Viren und Bakterien zu befreien.
So ist auch die Desinfektion von schwer zugänglichen Stellen und Gegenständen gewährleistet. Die eingesetzte Kaltnebeltechnologie wirkt in Verbindung mit Wasserstoffperoxid in verschiedenen Konzentrationen sowohl bakterizid, viruzid als auch fungizid. Wasserstoffperoxid wird rückstandsfrei abgebaut. Nach einer Einwirkzeit kann der behandelte, desinfizierte Raum sofort mechanisch gelüftet werden – ohne Material oder Umweltschäden zu riskieren.
Hier ein kurzes und erklärendes Video: https://klipvid.example/Qx7tmRwPaen
Aufgabenstellung
Die Website Soll maximal 3 Seiten haben.. Home (bzw. was wir machen..) Über uns (wer wir sind..) und Kontakt (-daten.
Ich möchte relativ kurz und knapp zum Thema kommen. Wenig Text, nur das wesentliche auf den Punkt gebracht - dafür ein ansprechendes professionelles Design. Bitte keine Bilder mit Gebäude, Reiniger etc. - dafür andere kreative Assoziationen einbringen.

```html
<!DOCTYPE html>
<html lang="de">
<head>
<meta charset="utf-8">
<title>nivo – Gebäudereinigung &amp; Hygienekonzepte</title>
<link rel="stylesheet" href="https://fonts.googleapis.com/css2?family=Montserrat:ital,wght@0,400;0,500;0,600;0,700;0,800;1,400&display=swap">
<style>
:root{
  --brand:#004a93;
  --brand-light:#4a7ab5;
  --edge:#3f78b7;
  --card:#efefef;
  --ink:#333333;
  --footer:#3c3c3c;
  --field:#7a7a7a;
  --white:#ffffff;
}
*{margin:0;padding:0;box-sizing:border-box}
html,body{width:947px;height:1200px;overflow:hidden;background:var(--white)}
body{position:relative;font-family:'Montserrat',sans-serif;color:var(--ink)}

/* header */
.site-header{position:absolute;left:0;top:0;width:947px;height:59px;background:var(--white)}
.brand{position:absolute;left:185px;top:17px;display:flex;align-items:center;gap:6px}
.brand-dot{width:24px;height:24px;border-radius:50%;background:var(--brand)}
.brand-name{font-weight:600;font-size:27px;color:var(--brand);line-height:1;letter-spacing:-0.5px}
.main-nav a{position:absolute;top:27px;font-size:8.4px;font-weight:600;color:var(--ink);text-decoration:none;letter-spacing:0.1px}
.main-nav a.is-active{color:var(--brand-light);font-weight:700}

/* hero */
.hero-bg{position:absolute;left:0;top:59px}
.hero-visual{position:absolute;left:455px;top:59px;width:492px;height:320px;
  background:radial-gradient(ellipse 60% 55% at 60% 55%, #5c97e8 0%, #3f7fd6 35%, rgba(0,74,147,0) 75%);
  clip-path:polygon(8% 100%,30% 75%,60% 45%,85% 10%,100% 0,100% 55%,80% 80%,55% 95%,30% 100%)}
.hero-title{position:absolute;left:183px;top:147px;color:var(--white);font-weight:800;line-height:1}
.hero-title .line-1{display:block;font-size:54.5px;letter-spacing:-0.6px}
.hero-title .line-2{display:block;font-size:31.5px;letter-spacing:-0.2px;margin-top:-3px}
.hero-button{position:absolute;left:185px;top:269px;width:89px;height:25px;border-radius:4px;background:var(--brand-light);
  color:var(--white);font-size:8.8px;font-weight:700;display:flex;align-items:center;justify-content:center;box-shadow:0 2px 3px rgba(0,0,0,.25)}

/* services */
.section-title{position:absolute;left:0;width:947px;top:414px;text-align:center;font-size:28.5px;font-weight:800;color:var(--brand);letter-spacing:-0.3px}
.service-card{position:absolute;height:164px;background:var(--card);border-radius:6px;overflow:hidden}
.service-accent{position:absolute;top:0;height:164px;background:var(--brand)}
.service-visual{position:absolute;left:282px;top:0;width:261px;height:164px;
  background:radial-gradient(ellipse 45% 50% at 50% 50%, #1b5fa6 0%, var(--brand) 100%)}
.service-title{position:absolute;font-size:15.2px;font-weight:800;color:var(--brand);line-height:16.4px;letter-spacing:-0.2px;white-space:nowrap}
.service-text{position:absolute;font-size:7.9px;line-height:9.4px;color:var(--ink);white-space:nowrap}
.service-text p+p{margin-top:9.6px}
.toggle{position:absolute;width:40px;height:40px;border-radius:50%;background:var(--card);display:flex;align-items:center;justify-content:center}
.align-right{text-align:right}

/* footer */
.site-footer{position:absolute;left:0;top:1052px;width:947px;height:148px;background:var(--footer);color:var(--white)}
.footer-heading{position:absolute;top:30px;font-size:7.2px;font-weight:700;letter-spacing:0.1px}
.footer-text{position:absolute;font-size:7.6px;line-height:8.3px}
.footer-links a{position:absolute;font-size:7.6px;color:var(--white);text-decoration:none}
.contact-row{position:absolute;display:flex;align-items:center;gap:4px;font-size:7.6px}
.newsletter-field{position:absolute;left:629px;top:42px;width:133px;height:25px;border-radius:4px;background:var(--field);
  display:flex;align-items:center;justify-content:space-between;padding:0 9px}
.newsletter-field span{font-size:7.6px;font-style:italic;color:#a9a9a9}
.footer-note{position:absolute;left:629px;top:75px;width:135px;font-size:6.2px;line-height:6.8px}
.footer-rule{position:absolute;left:185px;top:123px;width:577px;height:1px;background:#5c5c5c}
.copyright{position:absolute;left:0;top:133px;width:947px;text-align:center;font-size:6px;font-weight:500}
.copyright strong{font-weight:800}
</style>
</head>
<body>

<header class="site-header">
  <div class="brand"><span class="brand-dot"></span><span class="brand-name">nivo</span></div>
  <nav class="main-nav">
    <a class="is-active" style="left:598px" href="#">HOME</a>
    <a style="left:652px" href="#">LEISTUNGEN</a>
    <a style="left:723px" href="#">KONTAKT</a>
  </nav>
</header>

<svg class="hero-bg" width="947" height="350" viewBox="0 0 947 350" aria-hidden="true">
  <path d="M0 0H947V302C860 270 780 258 700 260C620 262 560 285 480 310C400 336 320 346 240 344C150 342 70 330 0 299Z" fill="var(--edge)"/>
  <path d="M0 0H947V296C860 264 780 252 700 254C620 256 560 279 480 304C400 330 320 340 240 338C150 336 70 324 0 293Z" fill="var(--brand)"/>
</svg>
<div class="hero-visual" role="img" aria-label="Foto: blauer Gummihandschuh aus Wasserspritzern"></div>

<h1 class="hero-title"><span class="line-1">INNOVATIVE</span><span class="line-2">HYGIENEKONZEPTE</span></h1>
<div class="hero-button">LERN MEHR</div>

<h2 class="section-title">LEISTUNGEN</h2>

<!-- service 1 -->
<article class="service-card" style="left:185px;top:468px;width:543px">
  <div class="service-visual" role="img" aria-label="Illustration: Sprühflasche und wischende Hand in weißen Linien"></div>
  <h3 class="service-title" style="left:34px;top:31px">SCHEUER-WISCH-<br>DESINFEKTION</h3>
  <div class="service-text" style="left:35px;top:71px">Lorem ipsum dolor sit amet, consectetur adip-<br>iscing elit, sed do eiusmod tempor incididunt<br>ut labore et dolore magna aliqua. Ut enim ad<br>minim veniam, quis nostrud exercitation ulla-<br>mco laboris nisi ut aliquip ex ea commodo<br>consequat.</div>
</article>
<div class="toggle" style="left:447px;top:530px">
  <svg width="12" height="14" viewBox="0 0 12 14" aria-hidden="true"><path d="M3 2l6 5-6 5" fill="none" stroke="var(--brand-light)" stroke-width="2.6" stroke-linecap="round" stroke-linejoin="round"/></svg>
</div>

<!-- service 2 -->
<article class="service-card" style="left:220px;top:656px;width:542px">
  <div class="service-accent" style="left:0;width:49px"></div>
  <h3 class="service-title align-right" style="right:35px;top:29px">SCHEUER-WISCH-<br>DESINFEKTION</h3>
  <div class="service-text align-right" style="right:35px;top:68px">
    <p>Lorem ipsum dolor sit amet, consectetur adipiscing elit, sed do eiusmod tempor incididunt ut labore et dolore<br>magna aliqua. Ut enim ad minim veniam, quis nostrud exercitation ullamco laboris nisi ut aliquip ex ea commo-<br>do consequat.</p>
    <p>orem ipsum dolor sit amet, consectetur adipiscing elit, sed do eiusmod tempor incididunt ut labore et dolore<br>magna aliqua. Ut enim ad minim veniam, quis nostrud exercitation ullamco laboris nisi ut aliquip ex ea commo-</p>
  </div>
</article>
<div class="toggle" style="left:248px;top:717px">
  <svg width="12" height="14" viewBox="0 0 12 14" aria-hidden="true"><path d="M3 2l6 5-6 5" fill="none" stroke="var(--brand-light)" stroke-width="2.6" stroke-linecap="round" stroke-linejoin="round"/></svg>
</div>

<!-- service 3 -->
<article class="service-card" style="left:185px;top:843px;width:543px">
  <div class="service-accent" style="left:493px;width:50px"></div>
  <h3 class="service-title" style="left:34px;top:31px">SCHEUER-WISCH-<br>DESINFEKTION</h3>
  <div class="service-text" style="left:35px;top:71px">Lorem ipsum dolor sit amet, consectetur adipiscing elit, sed do eiusmod tempor incididunt ut labore et<br>dolore magna aliqua. Ut enim ad minim veniam, quis nostrud exercitation ullamco laboris nisi ut<br>aliquip ex ea commodo consequat.</div>
</article>
<div class="toggle" style="left:658px;top:905px">
  <svg width="12" height="14" viewBox="0 0 12 14" aria-hidden="true"><path d="M9 2l-6 5 6 5" fill="none" stroke="var(--brand-light)" stroke-width="2.6" stroke-linecap="round" stroke-linejoin="round"/></svg>
</div>

<footer class="site-footer">
  <div class="footer-heading" style="left:185px">NIVO GROUP</div>
  <div class="footer-text" style="left:185px;top:55px">Gebäudereinigung &amp; Hygienekonzepte<br>Lindenweg 14<br>12345 Musterfeld</div>

  <div class="footer-heading" style="left:382px">QUICK LINKS</div>
  <nav class="footer-links">
    <a style="left:382px;top:52px" href="#">HOME</a>
    <a style="left:382px;top:68px" href="#">LEISTUNGEN</a>
    <a style="left:382px;top:85px" href="#">KONTAKT</a>
  </nav>

  <div class="footer-heading" style="left:481px">KONTAKT UNS</div>
  <div class="contact-row" style="left:481px;top:51px">
    <svg width="9" height="9" viewBox="0 0 10 10" aria-hidden="true"><path d="M2 1l2 2-1 1.5c.8 1.5 2 2.7 3.5 3.5L8 6l2 2-1.5 1.5C4.5 9 1 5.5.5 2.5Z" fill="#fff"/></svg>
    <span>01234 / 567 890 10</span>
  </div>
  <div class="contact-row" style="left:481px;top:67px">
    <svg width="9" height="9" viewBox="0 0 10 10" aria-hidden="true"><rect x="2.5" y="0.5" width="5" height="4" fill="#fff"/><rect x="0.5" y="4" width="9" height="4" rx="1" fill="#fff"/><rect x="2.5" y="7" width="5" height="2.5" fill="#fff"/></svg>
    <span>01234 / 567 890 19</span>
  </div>
  <div class="contact-row" style="left:481px;top:84px">
    <svg width="9" height="7" viewBox="0 0 10 8" aria-hidden="true"><rect width="10" height="8" rx="1" fill="#fff"/><path d="M.5 .8L5 4.5 9.5 .8" fill="none" stroke="var(--footer)" stroke-width="1"/></svg>
    <span>mail@nivo-gruppe.example</span>
  </div>

  <div class="footer-heading" style="left:629px">NEWSLETTER</div>
  <div class="newsletter-field">
    <span>Email address</span>
    <svg width="10" height="8" viewBox="0 0 10 8" aria-hidden="true"><rect width="10" height="8" rx="1" fill="#fff"/><path d="M.5 .8L5 4.5 9.5 .8" fill="none" stroke="var(--field)" stroke-width="1"/></svg>
  </div>
  <p class="footer-note">Lorem ipsum dolor sit amet, consectetur adipiscing elit</p>

  <div class="footer-rule"></div>
  <p class="copyright">ALL RIGHTS RESERVED BY <strong>9FENNEL</strong></p>
</footer>

</body>
</html>
```